Life Coaching Business Card

Please check out my website at www.lorettavanmeer.example. Ideally I would like to use the same colors that I used on the site to match my business cards i.e: pink, green, teal, white
I want the final design to include a picture of me and also to be appealing and eye catching. For the picture I submitted, you can crop it smaller to just have my face (exclude my chest) showing.
Industry/Entity Type
Business
Contact Information for Business Card
Loretta Vanmeer
Transformational Life Coach
web: www.lorettavanmeer.example
email: loretta@lorettavanmeer.example
Phone: 555-318-4072
Look and feel
Each slider illustrates characteristics of the customer's brand and the style your logo design should communicate.

```html
<!DOCTYPE html>
<html lang="en">
<head>
<meta charset="utf-8">
<title>Loretta Vanmeer – Business Card</title>
<link rel="stylesheet" href="https://fonts.googleapis.com/css2?family=Exo+2:wght@300;400;700&display=swap">
<style>
  :root {
    --lime: #b5d334;
    --lime-light: #d4ea4f;
    --lime-dark: #97bb1f;
    --pink: #e93fb9;
    --teal: #3dd3e3;
    --teal-dark: #22b7cf;
    --white: #ffffff;
    --paper: #f4f4f4;
    --ink: #2c2c2c;
    --ink-soft: #555555;
    --stage: #e9e7e3;
  }
  * { margin: 0; padding: 0; box-sizing: border-box; }
  html, body {
    width: 1200px; height: 1022px; overflow: hidden;
    background: var(--stage);
    font-family: "Exo 2", sans-serif;
  }
  .canvas { position: relative; width: 1200px; height: 1022px; }

  .card {
    position: absolute; left: 215px; width: 770px; height: 440px;
    border-radius: 6px; overflow: hidden;
    box-shadow: 0 6px 18px rgba(0,0,0,.18);
  }
  .card--front { top: 42px; background: linear-gradient(180deg, var(--white), var(--paper)); }
  .card--back  { top: 540px; }

  /* front */
  .front__panel {
    position: absolute; left: 0; top: 0; width: 330px; height: 440px;
    background: linear-gradient(135deg, var(--lime-light), var(--lime) 60%, var(--lime-dark));
  }
  .front__band {
    position: absolute; left: 0; bottom: 0; width: 770px; height: 80px;
    background: linear-gradient(90deg, var(--lime), var(--lime-light) 50%, var(--lime));
  }
  .portrait {
    position: absolute; left: 70px; top: 40px; width: 230px; height: 230px;
    border-radius: 50%;
    background: radial-gradient(circle at 55% 45%, #bdbdbd, #6a6a6a 60%, #2a2a2a);
    box-shadow: 0 0 0 4px rgba(255,255,255,.35);
  }
  .identity { position: absolute; left: 40px; top: 302px; }
  .identity__name {
    font-weight: 700; font-size: 27px; color: var(--ink);
    font-variant: small-caps; letter-spacing: 1px;
  }
  .identity__rule { width: 270px; height: 1px; background: rgba(255,255,255,.8); margin: 6px 0 6px; }
  .identity__title {
    font-weight: 300; font-size: 19px; color: var(--white);
    font-variant: small-caps; letter-spacing: 1px;
  }

  .dots { position: absolute; left: 360px; top: 36px; display: flex; gap: 18px; }
  .dot { width: 54px; height: 54px; border-radius: 50%; }
  .dot--lime { background: var(--lime); }
  .dot--pink { background: var(--pink); }
  .dot--teal { background: var(--teal); }

  .contacts { position: absolute; left: 300px; top: 160px; list-style: none; }
  .contact { display: flex; align-items: center; height: 62px; }
  .contact__tab {
    width: 60px; height: 50px; border-radius: 25px;
    background: var(--white);
    display: flex; align-items: center; justify-content: center;
    box-shadow: -2px 0 3px rgba(0,0,0,.08);
  }
  .contact__tab svg { width: 26px; height: 26px; }
  .contact__text {
    margin-left: 16px; font-weight: 300; font-size: 18px; color: var(--ink-soft);
    text-transform: uppercase; letter-spacing: .5px;
  }

  .edge-tab { position: absolute; right: 0; width: 34px; height: 54px; }
  .edge-tab--teal { top: 196px; background: var(--teal); border-radius: 12px 0 0 0; }
  .edge-tab--pink { top: 250px; background: var(--pink); height: 46px; }

  /* back */
  .back__lime  { position: absolute; left: 0; top: 0; width: 250px; height: 440px;
    background: linear-gradient(135deg, var(--lime-light), var(--lime)); }
  .back__white { position: absolute; left: 250px; top: 0; width: 80px; height: 440px; background: var(--white); }
  .back__teal  { position: absolute; left: 330px; top: 0; width: 440px; height: 440px;
    background: linear-gradient(135deg, var(--teal), var(--teal-dark)); }
</style>
</head>
<body>
<main class="canvas">

  <section class="card card--front" aria-label="Business card front">
    <div class="front__panel"></div>
    <div class="front__band"></div>

    <div class="portrait" role="img" aria-label="Black and white portrait photo of Loretta Vanmeer"></div>

    <div class="identity">
      <h1 class="identity__name">Loretta Vanmeer</h1>
      <div class="identity__rule"></div>
      <p class="identity__title">Transformational Life Coach</p>
    </div>

    <div class="dots">
      <span class="dot dot--lime"></span>
      <span class="dot dot--pink"></span>
      <span class="dot dot--teal"></span>
    </div>

    <ul class="contacts">
      <li class="contact">
        <span class="contact__tab">
          <svg viewBox="0 0 24 24" aria-hidden="true"><path fill="#2c2c2c" d="M6.6 2.5l3 3.2-1.9 2.4c1.2 2.6 3.2 4.6 5.8 5.9l2.4-1.9 3.2 3-2 3.4C10.5 18.1 5.4 13 4 5.5z"/></svg>
        </span>
        <span class="contact__text">Phone: 555-318-4072</span>
      </li>
      <li class="contact">
        <span class="contact__tab">
          <svg viewBox="0 0 24 24" aria-hidden="true" fill="none" stroke="#2c2c2c" stroke-width="1.6"><circle cx="12" cy="12" r="9" fill="#2c2c2c"/><g stroke="#fff" stroke-width="1"><ellipse cx="12" cy="12" rx="4" ry="9"/><path d="M3 12h18M4.5 7.5h15M4.5 16.5h15M12 3v18"/></g></svg>
        </span>
        <span class="contact__text">Web: www.lorettavanmeer.example</span>
      </li>
      <li class="contact">
        <span class="contact__tab">
          <svg viewBox="0 0 24 24" aria-hidden="true"><rect x="2" y="5" width="20" height="14" fill="#2c2c2c"/><path d="M2 5l10 8 10-8" fill="none" stroke="#fff" stroke-width="1.3"/></svg>
        </span>
        <span class="contact__text">Email: loretta@lorettavanmeer.example</span>
      </li>
    </ul>

    <span class="edge-tab edge-tab--teal"></span>
    <span class="edge-tab edge-tab--pink"></span>
  </section>

  <section class="card card--back" aria-label="Business card back">
    <div class="back__lime"></div>
    <div class="back__white"></div>
    <div class="back__teal"></div>
  </section>

</main>
</body>
</html>
```